7QK Pop Up Shop Clearance Flyer

We sell furniture. We opened up recently a temporary pop up shop to clear some stock we had from our old shop. So we don't have a full collection just our clearance lines that we want to get rid of - but the customer doesn't need to know this! Therefore the aim of this leaflet is to attract customers and make them come in - once they are there they might see something they like. As we will not be there for long - just a few more weeks.
We need a flyer to promote locally our pop up shop (temporary shop) with a Clearance Sale. The flyer will be sent by post or by hand to the local residents and by email to ex customers that bought from us before and we have their email address...
We need a modern fresh design flyer. At the next stage we will provide text for each item (brief description, dimensions and price) so allow some space for this.
Maybe we need to add a message or something to make people want to come quickly? For example most of the items are ex display or the last item and if they want it they should hurry as one is gone its gone. or you may have a better suggestion - let me know.
if you want to see some ideas of our website then 7QK.co.uk

Target Market(s)

Local Residents around shop

Industry/Entity Type

Retail

Colors
0255a3
3176b5
85abd2

Requirements
Must have
• price tag showing RRP or WAS price and the Clearance Sale price
• Opening Hours: Mon-Fri 9:00am - 5:00pm, Sat: 9:00am - 4:00pm, Sun: Closed
• Tel: 0208 915 2730
• Shop Address: 184 Birch Rowe, Elmwick Vale, London, N21 7PD
Nice to have
• Parking behind Bo Tarvins
• Map of location

```html
<!DOCTYPE html>
<html lang="en">
<head>
<meta charset="utf-8">
<title>7QK Pop Up Shop Clearance Sale</title>
<link href="https://fonts.googleapis.com/css2?family=Montserrat:wght@600;800;900&family=Roboto+Condensed:ital,wght@0,700;1,800;1,900&family=Kaushan+Script&family=Playfair+Display:wght@700&display=swap" rel="stylesheet">
<style>
:root{
  --blue-dark:#0255a3;
  --blue:#3176b5;
  --blue-light:#85abd2;
  --blue-pale:#e6eef7;
  --ink:#1d2b3a;
  --grey:#55606b;
  --white:#ffffff;
  --sofa:#7f8790;
  --chair:#b9b3aa;
}
*{box-sizing:border-box;margin:0;padding:0}
html,body{width:857px;height:1200px;overflow:hidden;background:var(--white)}
.flyer{position:relative;width:857px;height:1200px;font-family:'Montserrat',sans-serif;color:var(--ink);overflow:hidden;background:linear-gradient(180deg,var(--white) 0%,var(--blue-pale) 60%,var(--white) 100%)}
.abs{position:absolute}

/* header */
.popup-tag{left:270px;top:12px;width:310px;height:38px;background:var(--blue);color:var(--white);font-weight:800;font-size:26px;letter-spacing:2px;text-align:center;line-height:38px;border-radius:6px 6px 0 0}
.headline{left:40px;top:50px;height:88px;display:flex;align-items:center;gap:14px}
.headline .clearance{background:var(--blue-dark);color:var(--white);font-weight:900;font-size:76px;padding:0 24px;line-height:88px;border-radius:14px;letter-spacing:-1px}
.headline .sale{color:var(--blue-dark);font-weight:900;font-size:92px;letter-spacing:2px;line-height:88px}

/* hero */
.hero-claim{left:38px;top:148px;font-family:'Roboto Condensed',sans-serif;font-style:italic;font-weight:900;color:var(--blue-dark);font-size:62px;line-height:.95;text-shadow:2px 3px 0 var(--blue-light)}
.hero-claim .big{font-size:80px;display:block}
.limited{left:420px;top:150px;width:110px;height:110px}
.limited text{font-family:'Roboto Condensed',sans-serif;font-weight:900;font-style:italic;fill:var(--blue-dark)}
.tagline{left:40px;top:350px;font-family:'Kaushan Script',cursive;color:var(--blue);font-size:20px;white-space:nowrap}
.chair-photo{left:560px;top:145px;width:92px;height:200px;background:linear-gradient(180deg,#f4f4f2,#d9d6d0);border-radius:6px}
.price-claim{left:660px;top:150px;width:192px;font-weight:900;color:var(--blue-dark);font-size:25px;line-height:1.15}
.price-claim .small{display:block;font-size:16px;color:var(--blue);margin-top:6px;font-weight:800;line-height:1.2}
.hand-photo{left:655px;top:360px;width:202px;height:295px;background:linear-gradient(200deg,#2a2f36,#5c6570);border-radius:40px 0 0 30px}
.sign{left:672px;top:378px;width:165px;background:var(--white);border:3px solid var(--blue-dark);border-radius:10px;text-align:center;padding:12px 8px;color:var(--blue-dark);font-weight:800;font-size:14px;line-height:1.2}
.sign .today{display:block;font-family:'Kaushan Script',cursive;font-weight:400;font-size:36px;color:var(--blue);margin:6px 0;line-height:1.1}
.sign .note{display:block;font-size:11px;font-weight:600;color:var(--grey)}

/* products */
.product-name{font-weight:800;color:var(--blue-dark);font-size:20px;white-space:nowrap;line-height:1.2}
.product-name.small{font-size:16px}
.product-desc{font-size:12px;color:var(--grey);line-height:1.3;font-weight:600}
.product-photo{border-radius:6px}
.photo-sofa{background:linear-gradient(180deg,#c9cdd2,var(--sofa))}
.photo-chair{background:linear-gradient(180deg,#ece9e4,var(--chair))}
.photo-table{background:linear-gradient(180deg,#f1f1f1,#c8cbce)}
.price-tag{width:100px;height:100px;border-radius:50%;background:var(--white);border:4px solid var(--blue);box-shadow:0 0 0 3px var(--blue-light);display:flex;flex-direction:column;align-items:center;justify-content:center;text-align:center;line-height:1}
.price-tag .rrp{background:var(--blue-dark);color:var(--white);font-size:10px;font-weight:800;padding:2px 6px;border-radius:3px}
.price-tag .rrp s{font-size:12px}
.price-tag .now{font-size:11px;font-weight:800;color:var(--blue-dark);margin-top:4px}
.price-tag .now b{display:block;font-size:22px;font-weight:900}
.price-tag .save{font-size:8px;font-weight:800;color:var(--blue);margin-top:2px}

/* voucher */
.brand{left:28px;top:884px;width:180px;display:flex;flex-direction:column;align-items:center;gap:10px}
.brand .mark{width:80px;height:80px;background:var(--blue-dark)}
.brand .name{font-weight:800;font-size:17px;color:var(--blue-dark);letter-spacing:1px}
.voucher{left:220px;top:880px;width:615px;height:120px;border:3px dashed var(--blue);border-radius:10px;background:var(--white);display:flex;overflow:hidden}
.voucher .left{flex:1;padding:8px 16px;position:relative}
.voucher .brand-line{font-weight:800;font-size:11px;color:var(--blue-dark);letter-spacing:1px}
.voucher .title{font-weight:900;font-size:26px;color:var(--blue-dark);line-height:1.05;margin-top:3px}
.voucher .title span{display:block;font-size:14px;color:var(--blue);letter-spacing:2px}
.voucher .fine{font-size:8px;color:var(--grey);margin-top:4px;line-height:1.25;width:290px}
.voucher .seal{position:absolute;right:16px;top:14px;width:50px;height:50px;border-radius:50%;background:var(--blue-light)}
.voucher .right{width:200px;background:var(--blue-dark);color:var(--white);text-align:center;padding:6px 10px}
.voucher .words{font-family:'Playfair Display',serif;font-size:13px;letter-spacing:2px}
.voucher .amount{font-weight:900;font-size:40px;line-height:1}
.voucher .label{font-weight:800;font-size:12px;letter-spacing:2px;line-height:1.2}
.voucher .terms{font-size:8px;line-height:1.2;margin-top:3px;font-weight:600}

/* contact */
.phone{left:40px;top:1010px;display:flex;align-items:center;gap:12px;font-weight:900;font-size:32px;color:var(--blue-dark);line-height:1}
.phone svg{width:36px;height:36px}
.parking{left:40px;top:1054px;font-weight:800;font-size:18px;color:var(--blue)}
.address-band{left:0;top:1094px;width:857px;height:44px;background:var(--blue-dark);color:var(--white);font-weight:800;font-size:15px;line-height:44px;text-align:center;white-space:nowrap}
.hours{left:0;top:1152px;width:857px;text-align:center;font-weight:700;font-size:15px;color:var(--blue-dark)}
</style>
</head>
<body>
<main class="flyer">

  <header>
    <div class="abs popup-tag">POP UP SHOP</div>
    <h1 class="abs headline"><span class="clearance">Clearance</span><span class="sale">SALE</span></h1>
  </header>

  <section class="hero">
    <p class="abs hero-claim">You can't<br>buy better<span class="big">Anywhere!</span></p>
    <svg class="abs limited" viewBox="0 0 120 120" aria-label="Limited period only">
      <polygon points="60,4 72,24 95,15 94,39 116,48 100,65 112,86 88,90 84,114 62,102 40,116 34,92 10,88 20,66 4,48 26,39 26,15 48,24" fill="var(--white)" stroke="var(--blue-dark)" stroke-width="4"/>
      <text x="60" y="46" text-anchor="middle" font-size="18">LIMITED</text>
      <text x="60" y="70" text-anchor="middle" font-size="22">PERIOD</text>
      <text x="60" y="92" text-anchor="middle" font-size="18">ONLY</text>
    </svg>
    <p class="abs tagline">Offers that'll leave you sitting pretty at our expense!</p>
    <div class="abs chair-photo" role="img" aria-label="Photo of a white leather dining chair"></div>
    <p class="abs price-claim">Better prices than the internet...<span class="small">... and definitely better service!</span></p>
    <div class="abs hand-photo" role="img" aria-label="Photo of a gloved waiter's hand holding up a sign"></div>
    <div class="abs sign">VISIT OUR POP UP SHOP CLEARANCE OUTLET<span class="today">Today!</span><span class="note">while stocks last, be quick!</span></div>
  </section>

  <section class="products">
    <h2 class="abs product-name" style="left:28px;top:392px">Calder Corner Sofa</h2>
    <div class="abs product-photo photo-sofa" style="left:28px;top:425px;width:190px;height:75px" role="img" aria-label="Photo of a grey corner sofa"></div>
    <div class="abs price-tag" style="left:227px;top:422px"><span class="rrp">RRP <s>£000</s></span><span class="now">NOW<b>£000</b></span><span class="save">YOU SAVE £000</span></div>
    <div class="abs price-tag" style="left:335px;top:422px"><span class="rrp">RRP <s>£000</s></span><span class="now">NOW<b>£000</b></span><span class="save">YOU SAVE £000</span></div>
    <p class="abs product-desc" style="left:28px;top:530px;width:190px">Full description of furniture on sale with configurations and measurements.</p>

    <h2 class="abs product-name" style="left:446px;top:436px;font-size:18px">Elva Dining Table</h2>
    <div class="abs product-photo photo-table" style="left:450px;top:466px;width:150px;height:50px" role="img" aria-label="Photo of a glass dining table"></div>
    <p class="abs product-desc" style="left:446px;top:526px;width:200px">Full description of furniture on sale with configurations and measurements.</p>

    <h2 class="abs product-name" style="left:28px;top:584px">Marlow Sofa</h2>
    <div class="abs product-photo photo-sofa" style="left:28px;top:614px;width:300px;height:60px" role="img" aria-label="Photo of two grey fabric sofas"></div>
    <div class="abs price-tag" style="left:340px;top:586px"><span class="rrp">RRP <s>£000</s></span><span class="now">NOW<b>£000</b></span><span class="save">YOU SAVE £000</span></div>
    <p class="abs product-desc" style="left:452px;top:604px;width:190px">Full description of furniture on sale with configurations and measurements.</p>

    <h2 class="abs product-name small" style="left:28px;top:690px">Grey Fabric Dining Chair</h2>
    <div class="abs product-photo photo-chair" style="left:28px;top:722px;width:160px;height:85px" role="img" aria-label="Photo of grey fabric dining chairs"></div>
    <div class="abs price-tag" style="left:193px;top:716px"><span class="rrp">RRP <s>£000</s></span><span class="now">NOW<b>£000</b></span><span class="save">YOU SAVE £000</span></div>
    <p class="abs product-desc" style="left:28px;top:826px;width:260px">Full description of furniture on sale with configurations and measurements.</p>

    <h2 class="abs product-name small" style="left:305px;top:690px">Grey Fabric Dining Chair</h2>
    <div class="abs product-photo photo-chair" style="left:305px;top:722px;width:160px;height:85px" role="img" aria-label="Photo of grey fabric dining chairs"></div>
    <div class="abs price-tag" style="left:470px;top:716px"><span class="rrp">RRP <s>£000</s></span><span class="now">NOW<b>£000</b></span><span class="save">YOU SAVE £000</span></div>
    <p class="abs product-desc" style="left:305px;top:826px;width:260px">Full description of furniture on sale with configurations and measurements.</p>

    <h2 class="abs product-name small" style="left:585px;top:690px">Kestrel Coffee Table</h2>
    <div class="abs product-photo photo-table" style="left:585px;top:727px;width:155px;height:75px" role="img" aria-label="Photo of a glass coffee table"></div>
    <div class="abs price-tag" style="left:748px;top:716px"><span class="rrp">RRP <s>£000</s></span><span class="now">NOW<b>£000</b></span><span class="save">YOU SAVE £000</span></div>
    <p class="abs product-desc" style="left:585px;top:826px;width:255px">Full description of furniture on sale with configurations and measurements.</p>
  </section>

  <section class="offer">
    <div class="abs brand"><span class="mark"></span><span class="name">7QK FURNITURE</span></div>
    <div class="abs voucher">
      <div class="left">
        <p class="brand-line">7QK FURNITURE</p>
        <p class="title"><span>QUALITY CONTEMPORARY</span>FURNITURE<span>DISCOUNT VOUCHER</span></p>
        <p class="fine">Terms apply. Voucher valid in store only, one per household, cannot be exchanged for cash or used with any other offer.</p>
        <span class="seal"></span>
      </div>
      <div class="right">
        <p class="words">ONE HUNDRED</p>
        <p class="amount">£100</p>
        <p class="label">VOUCHER</p>
        <p class="terms">This voucher entitles the bearer to a £100 discount on any order for furniture over £1000</p>
      </div>
    </div>
  </section>

  <footer>
    <p class="abs phone">
      <svg viewBox="0 0 24 24" aria-hidden="true"><circle cx="12" cy="12" r="12" fill="var(--blue-dark)"/><path d="M8.2 5.5l2 2.6-1.2 1.6c.8 1.8 2.3 3.3 4.1 4.1l1.6-1.2 2.6 2-1 2c-4.6.2-9.6-4.8-9.4-9.4z" fill="var(--white)"/></svg>
      0208 915 2730
    </p>
    <p class="abs parking">Free Parking Behind Bo Tarvins</p>
    <p class="abs address-band">Temporary Pop Up Shop Address at 184 Birch Rowe, Elmwick Vale, London, N21 7PD</p>
    <p class="abs hours">Opening Hours: Mon-Fri 9:00am - 5:00pm, Sat: 9:00am - 4:00pm, Sun: Closed</p>
  </footer>

</main>
</body>
</html>
```